Social Media App Needs PPT Template

We need a PowerPoint template for a new social media company based in the DC area called "Clear Ledger." We provide an interactive digital platform for executives to share actionable advice. We would like to see designs that use our orange logo color as an accent, but are mainly grey, white, and black. The final design should communicate clean, chic, modern, and professional.

Target Market(s)

Executives

Industry/Entity Type

Information Technology

Font styles to use
Sans Serif

Colors
f78f20
fbe7d2
ffffff
000000
e8e8e8
757575

Requirements
Must have
• My project must have title page and many options for the body of the ppt (graphs, tables, etc). It also needs to be easy to modify. I must have someone who is experienced in creating powerpoint templates.
Nice to have
• It would be nice to have a very modern and clean design that includes the logo on every page, but still leaves a lot of room for the content of the slide
Should not have
• My design project should not look to busy.

```html
<!DOCTYPE html>
<html lang="en">
<head>
<meta charset="utf-8">
<title>Clear Ledger — Presentation Template Overview</title>
<link rel="stylesheet" href="https://fonts.googleapis.com/css2?family=Archivo:wght@500;700;800&family=Open+Sans:wght@400;600;700&display=swap">
<style>
  :root{
    --orange:#f78f20;
    --orange-deep:#f26a21;
    --peach:#fbe7d2;
    --white:#ffffff;
    --black:#000000;
    --ink:#1a1a1a;
    --light:#e8e8e8;
    --mid:#757575;
    --backdrop:#dcd9d9;
    --charcoal:#454545;
    --photo-suit:linear-gradient(135deg,#5a5f86 0%,#2c3052 45%,#1b1e33 100%);
    --photo-office:linear-gradient(160deg,#f1f2f4 0%,#c9ccd2 55%,#7d8089 100%);
    --photo-glass:linear-gradient(160deg,#9fc6db 0%,#3b7396 50%,#15344a 100%);
    --photo-crowd:linear-gradient(180deg,#fafafa 0%,#cfcfcf 50%,#3a3a3a 100%);
  }
  *{box-sizing:border-box;margin:0;padding:0}
  html,body{width:1200px;height:1200px;overflow:hidden}
  body{background:var(--backdrop);font-family:"Open Sans",Arial,sans-serif;color:var(--ink);position:relative}

  .slide{position:absolute;background:var(--white);overflow:hidden}
  .photo{position:absolute;display:block}
  .photo--suit{background:var(--photo-suit)}
  .photo--office{background:var(--photo-office)}
  .photo--glass{background:var(--photo-glass)}
  .photo--crowd{background:var(--photo-crowd)}

  .slide-title{position:absolute;font-family:"Archivo",Arial,sans-serif;font-weight:700;font-size:12px;color:var(--ink)}
  .display{position:absolute;font-family:"Archivo",Arial,sans-serif;font-weight:800;color:var(--ink);line-height:1.12;letter-spacing:.5px;text-transform:uppercase}
  .body-copy{position:absolute;font-size:3.6px;line-height:1.6;color:var(--mid)}
  .page-no{position:absolute;right:20px;bottom:8px;font-size:3.4px;font-weight:700;color:var(--ink)}
  .rule{position:absolute;height:1px;width:24px;background:var(--mid)}

  .logo{position:absolute;display:flex;align-items:center;gap:2px;font-family:"Archivo",Arial,sans-serif;font-weight:700;font-size:5px;color:var(--ink);white-space:nowrap}
  .logo__dot{width:5px;height:5px;border-radius:50%;background:var(--orange)}

  .meta{position:absolute;font-size:3.4px;line-height:1.65;color:var(--light)}
  .meta b{color:var(--ink);font-weight:700;margin-left:4px}
  .meta span{display:inline-block;width:14px;color:#bdbdbd}
  .tags{position:absolute;font-size:3px;color:var(--mid)}

  /* features slide */
  .features{position:absolute;left:0;top:58px;width:100%;display:flex;justify-content:space-around;padding:0 10px}
  .feature{width:62px;text-align:center;color:var(--white)}
  .feature__icon{width:18px;height:18px;margin:0 auto 12px;border:1px solid rgba(255,255,255,.55);display:flex;align-items:center;justify-content:center}
  .feature__name{font-size:5.4px;font-weight:600;margin-bottom:7px}
  .feature__text{font-size:3.4px;line-height:1.5;color:#b8b8c4;margin-bottom:10px}
  .feature__btn{display:inline-block;border:1px solid var(--white);font-size:3px;padding:1px 10px}
  .feature--active .feature__name{color:var(--orange)}
  .feature--active .feature__icon{border-color:var(--orange)}
  .feature--active .feature__btn{border-color:var(--orange)}

  .card-label{position:absolute;height:8px;font-size:3.4px;color:var(--white);display:flex;align-items:center;justify-content:center}
</style>
</head>
<body>

<!-- Row 1 -->
<section class="slide" style="left:26px;top:25px;width:339px;height:190px;background:#1f2233">
  <div class="photo photo--suit" role="img" aria-label="Executive in a suit holding a business card, darkened" style="inset:0;opacity:.55"></div>
  <div style="position:absolute;inset:0;background:rgba(20,20,28,.55)"></div>
  <div class="slide-title" style="left:27px;top:15px;color:var(--white);font-weight:500">Awesome Features</div>
  <div class="features">
    <div class="feature">
      <div class="feature__icon"><svg width="9" height="7" viewBox="0 0 9 7"><rect x=".5" y=".5" width="8" height="6" fill="none" stroke="#fff" stroke-width=".7"/><path d="M.5 .5 4.5 4 8.5 .5" fill="none" stroke="#fff" stroke-width=".7"/></svg></div>
      <div class="feature__name">Clean Design</div>
      <div class="feature__text">We've packed all the features you could want into one awesome set</div>
      <span class="feature__btn">Service 1</span>
    </div>
    <div class="feature feature--active">
      <div class="feature__icon"><svg width="9" height="7" viewBox="0 0 9 7"><rect x=".5" y=".5" width="8" height="6" fill="none" stroke="#f78f20" stroke-width=".7"/><path d="M1 6 3.5 3 5.5 5 7 3.5 8.5 5.5" fill="none" stroke="#f78f20" stroke-width=".7"/></svg></div>
      <div class="feature__name">Clean Design</div>
      <div class="feature__text">We've packed all the features you could want into one awesome</div>
      <span class="feature__btn">Service 2</span>
    </div>
    <div class="feature">
      <div class="feature__icon"><svg width="9" height="9" viewBox="0 0 9 9"><path d="M1.5 6V4.5a3 3 0 0 1 6 0V6" fill="none" stroke="#fff" stroke-width=".7"/><rect x="1" y="5" width="1.6" height="2.5" fill="#fff"/><rect x="6.4" y="5" width="1.6" height="2.5" fill="#fff"/></svg></div>
      <div class="feature__name">Clean Design</div>
      <div class="feature__text">We've packed all the features you could want into one awesome</div>
      <span class="feature__btn">Service 3</span>
    </div>
    <div class="feature">
      <div class="feature__icon"><svg width="9" height="9" viewBox="0 0 9 9"><path d="M2 1v7M4.5 1v7M7 1v7" stroke="#fff" stroke-width=".6"/><rect x="1.2" y="5" width="1.6" height="1.2" fill="#fff"/><rect x="3.7" y="2.5" width="1.6" height="1.2" fill="#fff"/><rect x="6.2" y="4" width="1.6" height="1.2" fill="#fff"/></svg></div>
      <div class="feature__name">Clean Design</div>
      <div class="feature__text">We've packed all the features you could want into one awesome</div>
      <span class="feature__btn">Service 4</span>
    </div>
  </div>
</section>

<section class="slide" style="left:424px;top:25px;width:340px;height:190px">
  <div class="photo photo--suit" role="img" aria-label="Close-up of an executive slipping a business card into a suit pocket" style="inset:0"></div>
  <div style="position:absolute;left:0;right:0;top:58px;text-align:center;color:var(--white)">
    <div style="font-size:3.6px;font-weight:700;letter-spacing:.3px">PRESENTATION</div>
    <div style="font-family:'Archivo',Arial,sans-serif;font-weight:500;font-size:16px;line-height:.98;margin-top:4px">ONLY<br>AWESOME<br>SLIDES</div>
    <div style="font-size:3.4px;margin-top:4px;color:#d0d0dc">We have the best selection of slides</div>
  </div>
</section>

<section class="slide" style="left:802px;top:25px;width:345px;height:194px">
  <svg class="photo" role="img" aria-label="Executive with business card seen through diagonal stripes" style="left:0;top:0" width="170" height="194" viewBox="0 0 170 194">
    <defs><linearGradient id="suitA" x1="0" y1="0" x2="1" y2="1"><stop offset="0" stop-color="#5a5f86"/><stop offset=".5" stop-color="#2c3052"/><stop offset="1" stop-color="#1b1e33"/></linearGradient>
      <clipPath id="stripesA"><path d="M-20 58 L150 0 L160 18 L-20 80Z M-20 100 L160 38 L166 58 L-20 122Z M-20 140 L165 78 L170 98 L-20 162Z M-20 180 L165 118 L160 140 L-20 200Z"/></clipPath></defs>
    <rect width="170" height="194" fill="url(#suitA)" clip-path="url(#stripesA)"/>
  </svg>
  <div class="logo" style="right:12px;top:12px"><span class="logo__dot"></span>Clear Ledger</div>
  <div class="display" style="right:22px;top:58px;font-size:25px;text-align:right">Our<br>Projects</div>
  <div class="body-copy" style="right:22px;top:117px;width:110px;text-align:right">Your first font choice often comes from the brand guide, so pick a clear typeface and keep it.</div>
  <div class="page-no">Page 28</div>
</section>

<!-- Row 2 -->
<section class="slide" style="left:26px;top:234px;width:339px;height:190px">
  <div class="slide-title" style="left:24px;top:19px;font-size:13px;font-weight:500">PROJECT X</div>
  <div class="meta" style="left:24px;top:50px"><span>DATE</span><b>MARCH 2016</b><br><span>CLIENT</span><b>NORTHFIELD</b><br><span>SIZE</span><b>1M AUDIENCE</b><br><span>FORMAT</span><b>VIDEO</b><br><span>MARKET</span><b>USA</b></div>
  <div class="tags" style="left:24px;top:108px">Art / Minimal / Typography / Placeholder</div>
  <div class="body-copy" style="left:24px;top:136px;width:86px">Your first font choice often comes from the brand guide, so pick a clear typeface and keep it.</div>
  <div class="photo photo--suit" role="img" aria-label="Hand placing a business card into a suit pocket" style="left:123px;top:0;width:106px;height:190px"></div>
  <div class="photo photo--crowd" role="img" aria-label="Businessman touching a virtual screen in front of a crowd" style="left:229px;top:0;width:110px;height:92px"></div>
  <div class="photo photo--office" role="img" aria-label="Business team in a meeting room presentation" style="left:229px;top:99px;width:110px;height:91px"></div>
</section>

<section class="slide" style="left:424px;top:234px;width:345px;height:194px">
  <div class="photo photo--office" role="img" aria-label="Business team in a meeting" style="left:0;top:0;width:107px;height:94px"></div>
  <div class="photo photo--crowd" role="img" aria-label="Businessman touching a virtual screen" style="left:0;top:100px;width:107px;height:94px"></div>
  <div class="photo photo--glass" role="img" aria-label="Businessman standing at a glass office window" style="left:112px;top:0;width:107px;height:194px"></div>
  <div class="slide-title" style="left:240px;top:20px;font-size:13px;font-weight:500">PROJECT X</div>
  <div class="logo" style="right:10px;top:20px"><span class="logo__dot"></span>Clear Ledger</div>
  <div class="meta" style="left:240px;top:52px"><span>DATE</span><b>MARCH 2016</b><br><span>CLIENT</span><b>BRIGHTWAVE</b><br><span>SIZE</span><b>1M AUDIENCE</b><br><span>FORMAT</span><b>VIDEO</b><br><span>MARKET</span><b>USA</b></div>
  <div class="tags" style="left:240px;top:111px">Art / Minimal / Typography / Placeholder</div>
  <div class="body-copy" style="left:240px;top:138px;width:86px">Your first font choice often comes from the brand guide, so pick a clear typeface and keep it.</div>
  <div class="page-no">Page 30</div>
</section>

<section class="slide" style="left:802px;top:234px;width:351px;height:198px">
  <div style="position:absolute;left:92px;top:24px;font-size:4.6px;font-weight:700">Awesome Placeholders</div>
  <div class="tags" style="left:92px;top:32px">Art / Minimal / Typography / Placeholder</div>
  <div class="body-copy" style="left:46px;top:53px;width:110px;text-align:right">Your first font choice comes from the brand guide.</div>
  <div class="photo photo--crowd" role="img" aria-label="Businessman touching a virtual screen in front of a crowd" style="left:176px;top:0;width:175px;height:99px"></div>
  <div class="photo photo--suit" role="img" aria-label="Hand placing a business card into a suit pocket" style="left:0;top:99px;width:176px;height:99px"></div>
  <div style="position:absolute;left:194px;top:114px;font-size:4.6px;font-weight:700">Awesome Placeholders</div>
  <div class="tags" style="left:194px;top:122px">Art / Minimal / Typography / Placeholder</div>
  <div class="body-copy" style="left:194px;top:142px;width:115px">Your first font choice comes from the brand guide.</div>
  <div class="page-no">Page 31</div>
</section>

<!-- Row 3 -->
<section class="slide" style="left:26px;top:452px;width:344px;height:194px">
  <div class="slide-title" style="left:28px;top:14px">Our Projects</div>
  <div class="logo" style="right:10px;top:18px"><span class="logo__dot"></span>Clear Ledger</div>
  <div style="position:absolute;left:28px;top:54px;font-size:7px;font-weight:700">Project X</div>
  <div class="body-copy" style="left:28px;top:72px;width:134px;text-align:justify">Your first font choice often comes from the brand guide, so pick a clear typeface and keep it. Your first font choice often comes from the brand guide, so pick a clear typeface and keep it.</div>
  <div class="photo photo--suit" role="img" aria-label="Hand placing a business card into a suit pocket" style="left:172px;top:46px;width:146px;height:119px"></div>
  <div class="page-no">Page 32</div>
</section>

<section class="slide" style="left:424px;top:452px;width:350px;height:197px">
  <div class="slide-title" style="left:29px;top:14px">Our Projects</div>
  <div class="logo" style="right:10px;top:18px"><span class="logo__dot"></span>Clear Ledger</div>
  <div class="photo photo--suit" role="img" aria-label="Business card in a suit pocket" style="left:41px;top:52px;width:84px;height:72px"></div>
  <div class="card-label" style="left:41px;top:124px;width:84px;background:var(--black)">Project 1</div>
  <div class="photo photo--crowd" role="img" aria-label="Businessman touching a virtual screen" style="left:133px;top:52px;width:85px;height:72px"></div>
  <div class="card-label" style="left:133px;top:124px;width:85px;background:var(--orange-deep)">Project 2</div>
  <div class="photo photo--office" role="img" aria-label="Team meeting in an office" style="left:226px;top:52px;width:84px;height:72px"></div>
  <div class="card-label" style="left:226px;top:124px;width:84px;background:#8a8a8a">Project 3</div>
  <div class="body-copy" style="left:41px;top:137px;width:84px">Your first font choice comes from the brand guide.</div>
  <div class="body-copy" style="left:133px;top:137px;width:85px">Your first font choice comes from the brand guide.</div>
  <div class="body-copy" style="left:226px;top:137px;width:84px">Your first font choice comes from the brand guide.</div>
  <div class="page-no">Page 38</div>
</section>

<section class="slide" style="left:802px;top:452px;width:357px;height:200px">
  <svg class="photo" role="img" aria-label="Business people in a bright office seen through diagonal stripes" style="left:0;top:0" width="190" height="200" viewBox="0 0 190 200">
    <defs><linearGradient id="officeB" x1="0" y1="0" x2="0" y2="1"><stop offset="0" stop-color="#e9eaee"/><stop offset=".5" stop-color="#6b6e76"/><stop offset="1" stop-color="#2b2d33"/></linearGradient>
      <clipPath id="stripesB"><path d="M0 30 L150 8 L158 22 L0 52Z M0 66 L162 30 L166 58 L0 100Z M0 114 L166 72 L170 104 L0 150Z M0 166 L166 120 L160 160 L40 200 L0 200Z"/></clipPath></defs>
    <rect width="190" height="200" fill="url(#officeB)" clip-path="url(#stripesB)"/>
  </svg>
  <div class="logo" style="right:16px;top:19px"><span class="logo__dot"></span>Clear Ledger</div>
  <div class="display" style="right:22px;top:60px;font-size:23px;text-align:right">Our<br>Charts</div>
  <div class="body-copy" style="right:22px;top:118px;width:110px;text-align:right">Your first font choice often comes from the brand guide, so pick a clear typeface and keep it.</div>
  <div class="page-no">Page 51</div>
</section>

<!-- Row 4 -->
<section class="slide" style="left:26px;top:662px;width:354px;height:198px">
  <div class="slide-title" style="left:28px;top:14px">Pie Charts</div>
  <div class="logo" style="right:10px;top:18px"><span class="logo__dot"></span>Clear Ledger</div>
  <svg style="position:absolute;left:20px;top:60px" width="320" height="50" viewBox="0 0 320 50">
    <g font-family="Open Sans, sans-serif" font-size="5" font-weight="700" text-anchor="middle" fill="#1a1a1a">
      <g transform="translate(42 25)"><circle r="20" fill="none" stroke="#e8e8e8" stroke-width="3.5"/><circle r="20" fill="none" stroke="#f26a21" stroke-width="3.5" stroke-dasharray="84.2 125.7" transform="rotate(-90)"/><text y="2">67 %</text></g>
      <g transform="translate(118 25)"><circle r="20" fill="none" stroke="#e8e8e8" stroke-width="3.5"/><circle r="20" fill="none" stroke="#f26a21" stroke-width="3.5" stroke-dasharray="46.5 125.7" transform="rotate(-90)"/><text y="2">37 %</text></g>
      <g transform="translate(194 25)"><circle r="20" fill="none" stroke="#e8e8e8" stroke-width="3.5"/><circle r="20" fill="none" stroke="#f26a21" stroke-width="3.5" stroke-dasharray="62.8 125.7" transform="rotate(-90)"/><text y="2">50 %</text></g>
      <g transform="translate(270 25)"><circle r="20" fill="none" stroke="#e8e8e8" stroke-width="3.5"/><circle r="20" fill="none" stroke="#f26a21" stroke-width="3.5" stroke-dasharray="109.4 125.7" transform="rotate(-90)"/><text y="2">87 %</text></g>
    </g>
  </svg>
  <div style="position:absolute;left:20px;top:126px;width:320px;display:flex;justify-content:space-around;text-align:center">
    <div style="width:46px"><div style="font-size:3.6px;font-weight:700">Design</div><div class="body-copy" style="position:static;margin-top:3px">Your first font choice comes from the brand.</div></div>
    <div style="width:46px"><div style="font-size:3.6px;font-weight:700">Design</div><div class="body-copy" style="position:static;margin-top:3px">Your first font choice comes from the brand.</div></div>
    <div style="width:46px"><div style="font-size:3.6px;font-weight:700">Design</div><div class="body-copy" style="position:static;margin-top:3px">Your first font choice comes from the brand.</div></div>
    <div style="width:46px"><div style="font-size:3.6px;font-weight:700">Design</div><div class="body-copy" style="position:static;margin-top:3px">Your first font choice comes from the brand.</div></div>
  </div>
  <div class="page-no">Page 52</div>
</section>

<section class="slide" style="left:424px;top:662px;width:353px;height:198px">
  <div class="slide-title" style="left:29px;top:14px">Bar Charts</div>
  <div class="logo" style="right:10px;top:18px"><span class="logo__dot"></span>Clear Ledger</div>
  <svg style="position:absolute;left:28px;top:66px" width="150" height="90" viewBox="0 0 150 90" font-family="Open Sans, sans-serif" font-size="2.6" fill="#757575">
    <g stroke="#e8e8e8" stroke-width=".4"><path d="M20 0V72M34 0V72M48 0V72M62 0V72M76 0V72M90 0V72M104 0V72M118 0V72M132 0V72"/></g>
    <g><rect x="20" y="6" width="112" height="3.6" fill="#454545"/><rect x="20" y="10" width="70" height="3.6" fill="#f26a21"/><rect x="20" y="14" width="42" height="3.6" fill="#000"/>
       <rect x="20" y="24" width="98" height="3.6" fill="#454545"/><rect x="20" y="28" width="84" height="3.6" fill="#f26a21"/><rect x="20" y="32" width="28" height="3.6" fill="#000"/>
       <rect x="20" y="42" width="70" height="3.6" fill="#454545"/><rect x="20" y="46" width="56" height="3.6" fill="#f26a21"/><rect x="20" y="50" width="28" height="3.6" fill="#000"/>
       <rect x="20" y="60" width="84" height="3.6" fill="#454545"/><rect x="20" y="64" width="28" height="3.6" fill="#f26a21"/><rect x="20" y="68" width="14" height="3.6" fill="#000"/></g>
    <text x="2" y="13">Name 4</text><text x="2" y="31">Name 3</text><text x="2" y="49">Name 2</text><text x="2" y="67">Name 1</text>
    <text x="19" y="78">0</text><text x="33" y="78">1</text><text x="47" y="78">2</text><text x="61" y="78">3</text><text x="75" y="78">4</text><text x="89" y="78">5</text><text x="103" y="78">6</text><text x="117" y="78">7</text><text x="131" y="78">8</text>
    <g transform="translate(60 86)"><rect width="2" height="2" fill="#000"/><text x="3" y="2">Series 1</text><rect x="14" width="2" height="2" fill="#f26a21"/><text x="17" y="2">Series 2</text><rect x="28" width="2" height="2" fill="#454545"/><text x="31" y="2">Series 3</text></g>
  </svg>
  <div class="display" style="left:192px;top:48px;font-size:18px">Awesome<br>Charts</div>
  <div class="rule" style="left:192px;top:102px"></div>
  <div class="body-copy" style="left:192px;top:112px;width:132px">Your first font choice often comes from the brand guide, so pick a clear typeface and keep it.</div>
  <div class="page-no">Page 53</div>
</section>

<section class="slide" style="left:802px;top:662px;width:362px;height:204px">
  <div class="slide-title" style="left:29px;top:14px">Creative Charts</div>
  <div class="logo" style="right:10px;top:18px"><span class="logo__dot"></span>Clear Ledger</div>
  <div class="display" style="left:31px;top:48px;font-size:18px">Awesome<br>Charts</div>
  <div class="rule" style="left:31px;top:104px"></div>
  <div class="body-copy" style="left:31px;top:122px;width:132px">Your first font choice often comes from the brand guide, so pick a clear typeface and keep it.</div>
  <svg style="position:absolute;left:200px;top:68px" width="150" height="110" viewBox="0 0 150 110" font-family="Open Sans, sans-serif" font-size="2.6" fill="#757575">
    <g><path d="M22 6h110l-110 5z" fill="#454545"/><path d="M22 10h70l-70 4z" fill="#f26a21"/><path d="M22 13h45l-45 3z" fill="#000"/>
       <path d="M22 24h90l-90 5z" fill="#454545"/><path d="M22 28h80l-80 4z" fill="#f26a21"/><path d="M22 31h30l-30 3z" fill="#000"/>
       <path d="M22 42h76l-76 5z" fill="#454545"/><path d="M22 46h58l-58 4z" fill="#f26a21"/><path d="M22 49h30l-30 3z" fill="#000"/>
       <path d="M22 60h86l-86 5z" fill="#454545"/><path d="M22 64h34l-34 4z" fill="#f26a21"/><path d="M22 67h18l-18 3z" fill="#000"/></g>
    <text x="4" y="11">Name 4</text><text x="4" y="29">Name 3</text><text x="4" y="47">Name 2</text><text x="4" y="65">Name 1</text>
    <text x="21" y="82">0</text><text x="51" y="82">2</text><text x="81" y="82">4</text><text x="111" y="82">6</text><text x="139" y="82">8</text>
    <g transform="translate(60 98)"><rect width="2" height="2" fill="#000"/><text x="3" y="2">Series 1</text><rect x="14" width="2" height="2" fill="#f26a21"/><text x="17" y="2">Series 2</text><rect x="28" width="2" height="2" fill="#454545"/><text x="31" y="2">Series 3</text></g>
  </svg>
  <div class="page-no">Page 54</div>
</section>

<!-- Row 5 -->
<section class="slide" style="left:26px;top:878px;width:356px;height:200px">
  <div class="slide-title" style="left:29px;top:14px">Creative Charts</div>
  <div class="logo" style="right:10px;top:18px"><span class="logo__dot"></span>Clear Ledger</div>
  <svg style="position:absolute;left:24px;top:64px" width="160" height="90" viewBox="0 0 160 90" font-family="Open Sans, sans-serif" font-size="2.6" fill="#757575">
    <g stroke="#e8e8e8" stroke-width=".4"><path d="M8 4H150M8 12H150M8 20H150M8 28H150M8 36H150M8 44H150M8 52H150M8 60H150M8 68H150M8 76H150"/></g>
    <g font-size="2.4"><text x="2" y="5">9</text><text x="2" y="13">8</text><text x="2" y="21">7</text><text x="2" y="29">6</text><text x="2" y="37">5</text><text x="2" y="45">4</text><text x="2" y="53">3</text><text x="2" y="61">2</text><text x="2" y="69">1</text><text x="2" y="77">0</text></g>
    <path d="M30 36 C45 40 50 48 62 40 S85 18 104 12 L130 6" fill="none" stroke="#454545" stroke-width=".8"/>
    <path d="M30 54 C40 54 48 58 62 50 S85 28 104 28 L130 36" fill="none" stroke="#f26a21" stroke-width=".8"/>
    <path d="M30 68 C45 64 50 60 62 58 S90 52 104 54 L130 52" fill="none" stroke="#454545" stroke-width=".8"/>
    <text x="29" y="83">1</text><text x="61" y="83">2</text><text x="103" y="83">3</text><text x="129" y="83">4</text>
    <g transform="translate(134 40)"><rect width="4" height=".8" y="1" fill="#000"/><text x="5" y="2">Series 1</text><rect width="4" height=".8" y="5" fill="#f26a21"/><text x="5" y="6">Series 2</text><rect width="4" height=".8" y="9" fill="#454545"/><text x="5" y="10">Series 3</text></g>
  </svg>
  <div class="display" style="left:194px;top:48px;font-size:18px">Awesome<br>Charts</div>
  <div class="rule" style="left:194px;top:102px"></div>
  <div class="body-copy" style="left:194px;top:120px;width:132px">Your first font choice often comes from the brand guide, so pick a clear typeface and keep it.</div>
  <div class="page-no">Page 55</div>
</section>

<section class="slide" style="left:424px;top:878px;width:361px;height:203px">
  <div class="slide-title" style="left:29px;top:14px">Creative Charts</div>
  <div class="logo" style="right:10px;top:18px"><span class="logo__dot"></span>Clear Ledger</div>
  <div class="display" style="left:31px;top:48px;font-size:18px">Awesome<br>Charts</div>
  <div class="rule" style="left:31px;top:102px"></div>
  <div class="body-copy" style="left:31px;top:122px;width:132px">Your first font choice often comes from the brand guide, so pick a clear typeface and keep it.</div>
  <svg style="position:absolute;left:196px;top:64px" width="150" height="110" viewBox="0 0 150 110" font-family="Open Sans, sans-serif" font-size="2.4" fill="#757575">
    <g stroke="#e8e8e8" stroke-width=".4"><path d="M14 6H140M14 18H140M14 30H140M14 42H140M14 54H140M14 66H140M14 78H140"/></g>
    <g><text x="2" y="7">14</text><text x="2" y="19">12</text><text x="2" y="31">10</text><text x="2" y="43">8</text><text x="2" y="55">6</text><text x="2" y="67">4</text><text x="2" y="79">2</text></g>
    <path d="M16 42 L56 42 L96 12 L136 12 L136 78 L16 78Z" fill="#454545"/>
    <path d="M16 62 L56 56 L96 36 L136 42 L136 78 L16 78Z" fill="#f26a21"/>
    <path d="M16 72 L56 68 L96 66 L136 70 L136 78 L16 78Z" fill="#000"/>
    <text x="10" y="84">Name 1</text><text x="50" y="84">Name 2</text><text x="90" y="84">Name 3</text><text x="128" y="84">Name 4</text>
    <g transform="translate(52 94)"><rect width="2" height="2" fill="#000"/><text x="3" y="2">Series 1</text><rect x="14" width="2" height="2" fill="#f26a21"/><text x="17" y="2">Series 2</text><rect x="28" width="2" height="2" fill="#454545"/><text x="31" y="2">Series 3</text></g>
  </svg>
  <div class="page-no">Page 56</div>
</section>

<section class="slide" style="left:802px;top:878px;width:370px;height:209px">
  <div class="slide-title" style="left:30px;top:14px">Bar Charts</div>
  <div class="logo" style="right:10px;top:18px"><span class="logo__dot"></span>Clear Ledger</div>
  <svg style="position:absolute;left:30px;top:70px" width="150" height="100" viewBox="0 0 150 100" font-family="Open Sans, sans-serif" font-size="2.4" fill="#757575">
    <g><text x="2" y="5">100%</text><text x="4" y="15">90%</text><text x="4" y="25">80%</text><text x="4" y="35">70%</text><text x="4" y="45">60%</text><text x="4" y="55">50%</text><text x="4" y="65">40%</text><text x="4" y="75">30%</text><text x="4" y="85">20%</text><text x="4" y="95">10%</text></g>
    <g><rect x="26" y="4" width="10" height="45" fill="#454545"/><rect x="26" y="49" width="10" height="27" fill="#f26a21"/><rect x="26" y="76" width="10" height="8" fill="#000"/>
       <rect x="56" y="4" width="10" height="38" fill="#454545"/><rect x="56" y="42" width="10" height="35" fill="#f26a21"/><rect x="56" y="77" width="10" height="7" fill="#000"/>
       <rect x="86" y="4" width="10" height="30" fill="#454545"/><rect x="86" y="34" width="10" height="38" fill="#f26a21"/><rect x="86" y="72" width="10" height="12" fill="#000"/>
       <rect x="116" y="4" width="10" height="36" fill="#454545"/><rect x="116" y="40" width="10" height="28" fill="#f26a21"/><rect x="116" y="68" width="10" height="16" fill="#000"/></g>
    <path d="M20 84H134" stroke="#e8e8e8" stroke-width=".4"/>
    <text x="25" y="90">Name 1</text><text x="55" y="90">Name 2</text><text x="85" y="90">Name 3</text><text x="115" y="90">Name 4</text>
    <g transform="translate(50 95)"><rect width="2" height="2" fill="#000"/><text x="3" y="2">Series 1</text><rect x="14" width="2" height="2" fill="#f26a21"/><text x="17" y="2">Series 2</text><rect x="28" width="2" height="2" fill="#454545"/><text x="31" y="2">Series 3</text></g>
  </svg>
  <div class="display" style="left:202px;top:50px;font-size:18px">Awesome<br>Charts</div>
  <div class="rule" style="left:202px;top:106px"></div>
  <div class="body-copy" style="left:202px;top:124px;width:135px">Your first font choice often comes from the brand guide, so pick a clear typeface and keep it.</div>
  <div class="page-no">Page 57</div>
</section>

</body>
</html>
```